Web-site design for company trading in chemicals & lubricants

We need a standard 5 page web-site designed for our company based in Dubai, UAE.
The web-site should highlight our capacity to store material as well as distribute the same. The products we sell are basic chemicals - packed in bags as well as drums. Bags are big bags - 25 kgs each as well as drums - 200 litres each. We want to highlight the fact that we huge stocks of this material & can deliver by sea & road,
Please use this site as a ref - http://www.norvex-solvents.co.uk/
Besides this, we need a page dedicated to finished products that we are selling for use in the auto industry - lubricants, motor oils,brake-fluids, greases, coolants etc. This are packed in large drums as well as small cans.
It would be nice if the site could immediately also provide a ref. to our location - Dubai or that we are based in the Middle East.
We will provide our company logo for reference

```html
<!DOCTYPE html>
<html lang="en">
<head>
<meta charset="utf-8">
<title>Korvant – Chemicals &amp; Lubricants</title>
<link rel="stylesheet" href="https://fonts.googleapis.com/css2?family=Montserrat:wght@400;500;700&display=swap">
<style>
:root{
  --brown:#6a3818;
  --brown-dark:#4b230c;
  --brown-text:#5a2e12;
  --gold:#d6b54c;
  --gold-light:#e8cf78;
  --ink:#222;
  --footer:#1e1e1e;
  --panel:#f1efef;
}
*{box-sizing:border-box;margin:0;padding:0}
html,body{width:1159px;height:1200px;overflow:hidden}
body{position:relative;font-family:"Montserrat",sans-serif;color:var(--ink);
  background:linear-gradient(#fff 540px,#f1f1f1 1000px)}
.abs{position:absolute}
.site-header{left:0;top:0;width:1159px;height:136px;background:linear-gradient(#f2f2f2,#d9d9d9)}
.brand{left:38px;top:58px;font-size:46px;font-weight:700;letter-spacing:2px;color:var(--brown)}
.brand-mark{left:290px;top:18px;width:46px;height:46px;border-radius:50%;background:var(--brown)}
.search{left:887px;top:52px;display:flex}
.search input,.field{border:1px solid #ccc;background:#fff;height:24px}
.search input{width:205px}
.btn-go{background:var(--brown-dark);color:#fff;font-size:13px;height:24px;padding:0 8px;line-height:24px;border:0;font-family:inherit}
.main-nav{left:0;top:136px;width:1159px;height:42px;background:var(--brown)}
.main-nav a{position:absolute;top:12px;color:#fff;text-decoration:none;font-size:15.5px}
.hero{left:35px;top:189px;width:1073px;height:344px;
  background:linear-gradient(90deg,#2d5fb0,#8a2a22 18%,#1f55b8 35%,#c9a9b8 55%,#2458b5 72%,#8b2b22 85%,#1e5bb8)}
.hero-caption{left:0;top:259px;width:1073px;height:85px;background:rgba(10,20,40,.6);color:#fff;
  font-size:18.5px;line-height:23px;padding:20px 150px 20px 30px}
.welcome{left:35px;top:553px;font-size:21px;font-weight:400;color:var(--brown-text)}
.intro{left:40px;top:596px;width:725px;font-size:12.3px;line-height:17.3px}
.intro p+p{margin-top:17px}
.category{position:absolute;top:716px;width:238px}
.category h3{height:30px;border-radius:3px;background:linear-gradient(#e4e4e4,#cfcfcf);text-align:center;
  font-weight:400;font-size:17px;line-height:30px;color:#333}
.category .photo{margin-top:13px;height:128px}
.category p{margin-top:10px;font-size:12.2px;line-height:17.5px}
.panel{position:absolute;background:var(--panel);border:1px solid #ddd}
.panel h4{font-weight:400;font-size:16px;padding:0 12px}
.finder{left:826px;top:555px;width:283px;height:136px}
.finder h4{height:40px;line-height:42px;background:linear-gradient(#e6e6e6,#d2d2d2);color:#333}
.finder label{position:absolute;left:14px;top:56px;font-size:12.6px}
.finder .row{position:absolute;left:14px;top:82px;display:flex}
.finder .field{width:206px}
.news{left:826px;top:703px;width:285px;height:264px}
.news h4{height:36px;line-height:38px;background:var(--gold);color:#3a2208;padding-left:18px;font-size:17px}
.news ul{list-style:none;padding:19px 22px 0 31px}
.news li{position:relative;font-size:11.6px;line-height:15.3px;margin-bottom:25px}
.news li::before{content:"";position:absolute;left:-12px;top:4px;border:4px solid transparent;border-left:5px solid var(--brown-dark);border-right:0}
.read-more{position:absolute;left:179px;top:224px;background:var(--brown-dark);color:#fff;font-size:13px;padding:3px 8px}
.site-footer{left:0;top:1004px;width:1159px;height:196px;background:var(--footer);color:#fff}
.site-footer h5{position:absolute;font-weight:400;font-size:16px}
.map{left:59px;top:48px;width:161px;height:100px;background:linear-gradient(135deg,#a9c7e6,#eadfb5 55%,#f4e18c)}
.btn-gold{position:absolute;background:linear-gradient(var(--gold-light),var(--gold));color:#222;font-size:13px;text-align:center;border:0;font-family:inherit}
.news-text{left:331px;top:54px;width:245px;font-size:11.4px;line-height:13.5px}
.foot-links{right:47px;top:42px;display:flex;gap:16px;font-size:11.4px}
.copy{right:48px;top:69px;font-size:11.6px}
.social{left:962px;top:102px;display:flex;gap:5px}
.social span{width:26px;height:26px;border-radius:3px;background:#6f8fb8}
</style>
</head>
<body>
<header class="site-header abs">
  <div class="brand abs">KORVANT</div>
  <div class="brand-mark abs"></div>
  <form class="search abs"><input type="text" aria-label="Search"><button class="btn-go" type="button">GO</button></form>
</header>
<nav class="main-nav abs">
  <a style="left:40px">Home</a><a style="left:150px">About Us</a><a style="left:287px">Products</a>
  <a style="left:434px">Logistics</a><a style="left:571px">Business Fields</a><a style="left:760px">Contact Us</a>
</nav>
<section class="hero abs" role="img" aria-label="Warehouse racks stacked with blue and red chemical drums">
  <div class="hero-caption abs">Lorem ipsum dolor sit amet, consectetur adipisicing elit, sed do eiusmod tempor consectetur adipisicing incididunt ut ....</div>
</section>
<h2 class="welcome abs">Welcome to Our Site!</h2>
<div class="intro abs">
  <p>Lorem ipsum dolor sit amet, consectetur adipisicing elit, sed do eiusmod tempor incididunt ut labore et dolore magna aliqua. Ut enim ad minim veniam, quis nostrud exercitation ullamco laboris nisi ut aliquip ex ea commodo consequat.Lorem ipsum dolor sit amet, consectetur adipisicing elit, sed do eiusmod tempor incididunt</p>
  <p>Ut labore et dolore magna aliqua. Ut enim ad minim veniam, quis nostrud exercitation ullamco laboris nisi ut aliquip ex ea commodo consequat.</p>
</div>
<article class="category" style="left:40px"><h3>Motor Oils</h3>
  <div class="photo" role="img" aria-label="Motor oil poured from a can into a yellow funnel" style="background:linear-gradient(90deg,#555,#bfc3c8 40%,#e8b820 75%,#333)"></div>
  <p>Ut labore et dolore magna aliqua. Ut enim ad minim veniam, quis nostrud on ullamco laboris nisi ut aliquip ex ea commodo consequat...</p></article>
<article class="category" style="left:294px"><h3>Brake Fluids</h3>
  <div class="photo" role="img" aria-label="Brake disc and caliper" style="background:radial-gradient(circle at 55% 55%,#c8ccd2,#3c4656 60%,#111a26)"></div>
  <p>Ut labore et dolore magna aliqua. Ut enim ad minim veniam, quis nostrud on ullamco laboris nisi ut aliquip ex ea commodo consequat...</p></article>
<article class="category" style="left:550px"><h3>Greases</h3>
  <div class="photo" role="img" aria-label="Car engine bay" style="background:radial-gradient(circle at 50% 50%,#9aa3ab,#3a424a 60%,#1a2028)"></div>
  <p>Ut labore et dolore magna aliqua. Ut enim ad minim veniam, quis nostrud on ullamco laboris nisi ut aliquip ex ea commodo consequat...</p></article>
<aside class="panel finder"><h4>Product Finder</h4><label>Enter text</label>
  <div class="row"><input class="field" type="text" aria-label="Product"><button class="btn-go" type="button">GO</button></div></aside>
<aside class="panel news"><h4>Latest News</h4>
  <ul><li>Ut labore et dolore magna aliqua. Ut en im ad minim veniam, quis nostrud onu llamco laboris nisi ut aliquip ex ea commodo consequat...</li>
  <li>Ut labore et dolore magna aliqua. Ut en im ad minim veniam, quis nostrud onu llamco laboris nisi ut aliquip ex ea commodo consequat...</li></ul>
  <span class="read-more">Read more..</span></aside>
<footer class="site-footer abs">
  <h5 style="left:59px;top:17px">Location</h5>
  <div class="map abs" role="img" aria-label="Street map showing the company location"></div>
  <span class="btn-gold" style="left:136px;top:155px;width:83px;height:22px;line-height:22px">View map</span>
  <h5 style="left:331px;top:20px">Newsletter</h5>
  <p class="news-text abs">Ut labore et dolore magna aliqua. Ut enim ad minim veniam, quis nostru dolore magna ..</p>
  <input class="field abs" style="left:333px;top:108px;width:239px;height:25px" type="email" aria-label="Email">
  <span class="btn-gold" style="left:405px;top:154px;width:90px;height:21px;line-height:21px">Subscribe</span>
  <nav class="foot-links abs"><span>Home</span><span>About Us</span><span>Products</span><span>Logistics</span><span>Business Fields</span><span>Contact Us</span></nav>
  <p class="copy abs">Copyright @ 2011 Korvant.com. All Rights Reserved.</p>
  <div class="social abs"><span></span><span></span><span></span><span></span><span></span></div>
</footer>
</body>
</html>
```